Marrowgate Auctions Business Cards Design Needed

I need a business card design that is modern looking - double sided (maybe just my logo on the back, but open to suggestions) - the overall design is up to you. I want it to be easy to read - not over the top flashy. I already have a company logo which I uploaded so that needs to be used. The colors of my logo are the colors I want on the card... so blue and gray (do need to match the logo colors).

Requirements
Must have
• Would like the card to be sleek, modern and easy to ready

```html
<!DOCTYPE html>
<html lang="en">
<head>
<meta charset="utf-8">
<title>Marrowgate Auctions – Business Cards</title>
<link href="https://fonts.googleapis.com/css2?family=Work+Sans:wght@400;500;600&display=swap" rel="stylesheet">
<style>
  :root {
    --stage: #1b1b1c;
    --card: #2a2a2b;
    --card-edge: #333334;
    --brand-blue: #1f7fcf;
    --brand-gray: #a9abae;
    --ink: #f1f1f1;
  }
  * { box-sizing: border-box; margin: 0; padding: 0; }
  html, body { width: 1200px; height: 900px; overflow: hidden; }
  body {
    background: var(--stage);
    font-family: "Work Sans", Arial, sans-serif;
    color: var(--ink);
    position: relative;
  }
  .card {
    position: absolute;
    left: 250px;
    width: 700px;
    height: 400px;
    background: var(--card);
    border: 1px solid var(--card-edge);
    box-shadow: 0 18px 40px rgba(0,0,0,.55);
  }
  .card--back { top: 40px; }
  .card--front { top: 470px; }

  /* Back */
  .back-brand {
    position: absolute;
    top: 150px; left: 0; right: 0;
    text-align: center;
    font-weight: 600;
    font-size: 44px;
    letter-spacing: 1px;
    color: var(--brand-gray);
    text-transform: uppercase;
  }
  .back-tagline {
    position: absolute;
    top: 318px; left: 0; right: 0;
    text-align: center;
    font-size: 17px;
    font-weight: 500;
    letter-spacing: 1.5px;
    text-transform: uppercase;
  }

  /* Front */
  .front-brand {
    position: absolute;
    top: 62px; right: 50px;
    display: flex; align-items: center; gap: 12px;
    font-weight: 600;
    font-size: 26px;
    letter-spacing: .5px;
    text-transform: uppercase;
    color: var(--brand-blue);
  }
  .front-brand .brand-dot {
    width: 14px; height: 14px;
    background: var(--brand-blue);
  }
  .person-name {
    position: absolute;
    top: 150px; left: 60px;
    font-size: 38px;
    font-weight: 500;
    color: var(--brand-blue);
    text-transform: uppercase;
    line-height: 1;
  }
  .person-title {
    position: absolute;
    top: 196px; left: 60px;
    font-size: 19px;
    letter-spacing: .5px;
  }
  .divider {
    position: absolute;
    top: 236px; left: 55px; right: 50px;
    height: 2px;
    background: var(--brand-blue);
  }
  .contact-list {
    position: absolute;
    top: 258px; left: 60px;
    list-style: none;
  }
  .contact-list li {
    display: flex; align-items: center; gap: 12px;
    font-size: 19px;
    height: 30px;
    letter-spacing: .3px;
  }
  .contact-list svg { width: 14px; height: 14px; flex: none; }
  .location {
    position: absolute;
    bottom: 40px; right: 50px;
    font-size: 21px;
    letter-spacing: .5px;
  }
</style>
</head>
<body>

<section class="card card--back" aria-label="Card back">
  <div class="back-brand">Marrowgate Auctions</div>
  <div class="back-tagline">Improving charity auctions nationwide</div>
</section>

<section class="card card--front" aria-label="Card front">
  <div class="front-brand"><span class="brand-dot"></span>Marrowgate Auctions</div>

  <h1 class="person-name">Nolan Brandt</h1>
  <p class="person-title">Owner/President - Auctioneer</p>
  <div class="divider"></div>

  <ul class="contact-list">
    <li>
      <svg viewBox="0 0 14 14" aria-hidden="true"><path d="M3 1 L5.5 1 L6 4 L4.5 5 C5.3 7 7 8.7 9 9.5 L10 8 L13 8.5 L13 11 C13 12 12 13 11 13 C5.5 12.5 1.5 8.5 1 3 C1 2 2 1 3 1 Z" fill="var(--brand-blue)"/></svg>
      555-014-2298
    </li>
    <li>
      <svg viewBox="0 0 14 14" aria-hidden="true"><rect x="1" y="3" width="12" height="8" fill="none" stroke="var(--brand-blue)" stroke-width="1.4"/><path d="M1 3 L7 8 L13 3" fill="none" stroke="var(--brand-blue)" stroke-width="1.4"/></svg>
      hello@marrowgatebids.com
    </li>
    <li>
      <svg viewBox="0 0 14 14" aria-hidden="true"><circle cx="7" cy="7" r="5.6" fill="none" stroke="var(--brand-blue)" stroke-width="1.3"/><ellipse cx="7" cy="7" rx="2.4" ry="5.6" fill="none" stroke="var(--brand-blue)" stroke-width="1.1"/><path d="M1.4 7 H12.6" stroke="var(--brand-blue)" stroke-width="1.1"/></svg>
      www.marrowgatebids.com
    </li>
  </ul>

  <p class="location">Cedar Hollow, WA</p>
</section>

</body>
</html>
```